Modern business card and stationary for a dental office
World Class Care
Modern business card and stationary for a dental office - Health
Creative Brief
Professional
Dr. Martin Hollis
General Dentist
45870- 213 Street N.W. Edmonton, AB T6K 3R2
drhollis@brookvaledental.ca
brookvaledental.ca
Family Clinic *Cosmetic Dentistry *Implant Dentistry *services provided by a general dentist

```html
<!DOCTYPE html>
<html lang="en">
<head>
<meta charset="utf-8">
<title>Brookvale Dental – Business Card</title>
<link href="https://fonts.googleapis.com/css2?family=Montserrat:wght@400;600;700&family=Open+Sans:wght@400;600&display=swap" rel="stylesheet">
<style>
  :root{
    --stage:#2a2c30;
    --navy:#123a66;
    --navy-deep:#0b2748;
    --sky:#2ea6dd;
    --ink:#3a3f46;
    --muted:#6b727b;
    --paper:#ffffff;
    --silver-top:#fbfbfc;
    --silver-bottom:#d9dce0;
  }
  *{box-sizing:border-box;margin:0;padding:0}
  html,body{width:1200px;height:871px;overflow:hidden}
  body{
    background:var(--stage);
    font-family:"Open Sans",Arial,sans-serif;
    position:relative;
  }
  .card{
    position:absolute;
    left:270px;
    width:660px;height:377px;
    border-radius:22px;
    overflow:hidden;
    box-shadow:0 10px 30px rgba(0,0,0,.45);
  }
  .card--back{top:30px;background:linear-gradient(160deg,var(--silver-top),var(--silver-bottom))}
  .card--front{top:464px;background:var(--paper)}

  .brand{
    position:absolute;
    text-align:center;
    font-family:"Montserrat",Arial,sans-serif;
    font-weight:700;
    color:var(--navy);
  }
  .brand__dot{
    display:block;
    width:34px;height:34px;border-radius:50%;
    background:var(--navy);
    margin:0 auto 12px;
  }
  .brand__name{font-size:40px;letter-spacing:.5px;line-height:1}
  .brand__sub{font-size:20px;letter-spacing:12px;margin-top:6px;line-height:1}

  .card--back .brand{left:40px;top:100px}
  .services{
    position:absolute;right:36px;top:138px;
    text-align:right;
    font-family:"Open Sans",Arial,sans-serif;
    color:var(--ink);
    font-size:17px;line-height:1.75;
  }
  .services__title{font-family:"Montserrat",Arial,sans-serif;font-weight:700;color:var(--navy);font-size:16px;margin-bottom:6px}
  .services__item::after{
    content:"";display:inline-block;width:7px;height:7px;border-radius:50%;
    background:var(--navy);margin-left:12px;vertical-align:middle;
  }

  .front__waves{position:absolute;inset:0}
  .card--front .brand{left:32px;top:108px}
  .divider{position:absolute;left:318px;top:150px;width:1px;height:190px;background:#c7cbd0}

  .person{
    position:absolute;right:30px;top:62px;text-align:right;color:#fff;
    font-family:"Montserrat",Arial,sans-serif;
  }
  .person__name{font-size:19px;font-weight:700;line-height:1.3}
  .person__role{font-size:13px;font-weight:600;margin-top:4px}

  .contact{
    position:absolute;left:336px;top:164px;
    color:var(--ink);font-size:14.5px;line-height:1.55;
  }
  .contact__address{margin-bottom:8px}
  .contact__row{display:flex;align-items:center;gap:10px}
  .contact__icon{width:15px;height:15px;fill:var(--muted);flex:none}
</style>
</head>
<body>

<section class="card card--back" aria-label="Card back">
  <div class="brand">
    <span class="brand__dot"></span>
    <div class="brand__name">BROOKVALE</div>
    <div class="brand__sub">DENTAL</div>
  </div>
  <div class="services">
    <div class="services__title">Family Clinic</div>
    <div class="services__item">Cosmetic Dentistry</div>
    <div class="services__item">Implant Dentistry</div>
    <div class="services__item">General dentist</div>
  </div>
</section>

<section class="card card--front" aria-label="Card front">
  <svg class="front__waves" viewBox="0 0 660 377" preserveAspectRatio="none" aria-hidden="true">
    <defs>
      <linearGradient id="bandNavy" x1="0" y1="0" x2="1" y2="1">
        <stop offset="0" stop-color="#1d5089"/>
        <stop offset="1" stop-color="#0b2748"/>
      </linearGradient>
    </defs>
    <path d="M30 0 C250 8 460 50 660 380 V0 Z" fill="var(--sky)"/>
    <path d="M56 0 C265 4 470 40 660 355 V0 Z" fill="#ffffff"/>
    <path d="M76 0 C280 0 480 30 660 330 V0 Z" fill="url(#bandNavy)"/>
  </svg>

  <div class="person">
    <div class="person__name">Dr. Martin Hollis</div>
    <div class="person__role">General Dentist</div>
  </div>

  <div class="brand">
    <span class="brand__dot"></span>
    <div class="brand__name">BROOKVALE</div>
    <div class="brand__sub">DENTAL</div>
  </div>

  <div class="divider"></div>

  <div class="contact">
    <div class="contact__address">45870- 213 Street N.W.<br>Edmonton, AB T6K 3R2</div>
    <div class="contact__row">
      <svg class="contact__icon" viewBox="0 0 24 24"><path d="M6.6 10.8a15.1 15.1 0 0 0 6.6 6.6l2.2-2.2c.3-.3.7-.4 1-.2 1.1.4 2.3.6 3.6.6.6 0 1 .4 1 1V20c0 .6-.4 1-1 1A17 17 0 0 1 3 4c0-.6.4-1 1-1h3.5c.6 0 1 .4 1 1 0 1.3.2 2.5.6 3.6.1.3 0 .7-.2 1z"/></svg>
      <span>780-555-0142</span>
    </div>
    <div class="contact__row">
      <svg class="contact__icon" viewBox="0 0 24 24"><path d="M6 2h9l3 3v4H6z M3 10h18v9H3z M7 13h2v2H7z M11 13h2v2h-2z M15 13h2v2h-2z M6 20h12v2H6z"/></svg>
      <span>780-555-0187</span>
    </div>
    <div class="contact__row">
      <svg class="contact__icon" viewBox="0 0 24 24"><path d="M2 5h20v14H2z M3.5 6.5 12 13l8.5-6.5" stroke="#fff" stroke-width="1.4"/></svg>
      <span>drhollis@brookvaledental.ca</span>
    </div>
    <div class="contact__row">
      <svg class="contact__icon" viewBox="0 0 24 24"><circle cx="12" cy="12" r="10"/><path d="M2 12h20M12 2c3 3 3 17 0 20M12 2c-3 3-3 17 0 20" stroke="#fff" stroke-width="1.3" fill="none"/></svg>
      <span>www.brookvaledental.ca</span>
    </div>
  </div>
</section>

</body>
</html>
```